Etiketten-Design für Trinkweine
Zielgruppe
Wir sind eine Weinkellerei, die einfache Trinkweine für den LEH herstellt.
Unsere Zielgruppen sind Jugendliche .
Wir suchen ein Etikett für unser neues Produkt ,,Traubensaftschorle`` alkoholfrei
Aufgabenstellung
Siehe Anhang , eigene ideen sind auch erwünscht.
Das Etikett sollte Natur verbunden wirken da es ein Bio Produkt ist.
Farben: weiß, grün wären erwünscht.
Das Etikett sollte 75mm hoch und 120mm Breit sein
Strukturpapier weiß
Anbei auch unserer Standartetikett gerne kann das Logo übernommen werden

```html
<!DOCTYPE html>
<html lang="de">
<head>
<meta charset="utf-8">
<title>Traubensaft Etikett – Weingut Martin Brauer</title>
<link rel="stylesheet" href="https://fonts.googleapis.com/css2?family=Michroma&family=Roboto:wght@400&display=swap">
<style>
  :root {
    --cream: #f8f6cc;
    --green-fresh: #6cb52f;
    --green-soft: #72bd7c;
    --green-dark: #1f5a2a;
    --stage: #ffffff;
  }
  * { box-sizing: border-box; margin: 0; padding: 0; }
  html, body {
    width: 1200px; height: 792px; overflow: hidden;
    background: var(--stage);
  }
  .canvas {
    position: relative; width: 1200px; height: 792px;
  }
  .label {
    position: absolute; left: 320px; width: 560px; height: 350px;
    background: var(--label-green);
    box-shadow: 0 3px 8px rgba(0,0,0,0.18);
    overflow: hidden;
    font-family: "Michroma", "Roboto", sans-serif;
  }
  .label--fresh { top: 21px; --label-green: var(--green-fresh); }
  .label--soft  { top: 421px; --label-green: var(--green-soft); }

  .label__brand {
    position: absolute; top: 0; left: 95px; width: 366px; height: 118px;
    display: flex; align-items: center; justify-content: center;
    white-space: nowrap;
  }
  .brand-name {
    font-size: 20px; color: var(--cream); letter-spacing: 1px;
    text-transform: uppercase;
  }
  .label__seal {
    position: absolute; top: 22px; left: 462px; width: 72px; height: 72px;
    border-radius: 50%; background: var(--green-dark); opacity: 0.85;
  }
  .label__dots {
    position: absolute; top: 118px; left: 0; width: 100%; height: 20px;
    background-color: var(--cream);
    background-image: radial-gradient(circle, var(--label-green) 5px, transparent 5.5px);
    background-size: 49px 20px;
    background-position: 6px 0;
  }
  .label__title {
    position: absolute; top: 156px; left: 95px; width: 366px;
    text-align: center; color: var(--cream);
    font-size: 32px; line-height: 50px; font-weight: 400;
    white-space: nowrap;
  }
  .label__note {
    position: absolute; top: 266px; left: 95px; width: 366px;
    text-align: center; color: var(--cream);
    font-family: "Roboto", sans-serif; font-size: 9px;
  }
  .label__window {
    position: absolute; top: 171px; left: 421px; width: 118px; height: 136px;
    background: var(--cream);
  }
  .label__address {
    position: absolute; top: 277px; left: 14px;
    font-family: "Roboto", sans-serif; font-size: 9px; line-height: 11.5px;
    color: var(--green-dark); font-style: normal;
  }
  .label__footer {
    position: absolute; bottom: 0; left: 0; width: 100%; height: 37px;
    background: var(--cream);
    display: flex; align-items: center; justify-content: space-between;
    padding: 0 36px 0 14px;
  }
  .vos { font-family: "Roboto", sans-serif; font-size: 11px; color: #222; }
  .volume { font-size: 18px; color: var(--green-dark); }
</style>
</head>
<body>
<main class="canvas">

  <section class="label label--fresh">
    <div class="label__brand"><span class="brand-name">Martin Brauer</span></div>
    <div class="label__seal" role="img" aria-label="Siegel 100 % natürlich mit Trauben"></div>
    <div class="label__dots"></div>
    <h1 class="label__title">TRAUBEN<br>SAFT</h1>
    <p class="label__note">(mit zugesetzter Kohlensäure)</p>
    <div class="label__window"></div>
    <address class="label__address">Weingut Martin Brauer<br>Lindenweg 4b<br>79100 Talheim</address>
    <div class="label__footer"><span class="vos">VOS Nr. 01/20</span><span class="volume">0.33l</span></div>
  </section>

  <section class="label label--soft">
    <div class="label__brand"><span class="brand-name">Martin Brauer</span></div>
    <div class="label__seal" role="img" aria-label="Siegel 100 % natürlich mit Trauben"></div>
    <div class="label__dots"></div>
    <h2 class="label__title">TRAUBEN<br>SAFT</h2>
    <p class="label__note">(mit zugesetzter Kohlensäure)</p>
    <div class="label__window"></div>
    <address class="label__address">Weingut Martin Brauer<br>Lindenweg 4b<br>79100 Talheim</address>
    <div class="label__footer"><span class="vos">VOS Nr. 01/20</span><span class="volume">0.33l</span></div>
  </section>

</main>
</body>
</html>
```